Exercise Physiologist needs business cards

I have a logo, I need business cards (Sole trader) as I am moving to a new location and would like an updated look. I provide gym based exercise rehabilitation, injury prevention and movement assessments. I have over 13 years experience as an Exercise Physiologist. I would like the cards to look professional but not boring and can be a little different to stand out when sitting with other Allied Health Professional cards.

Target Market(s)

GP's, Allied health practitioners, people with injuries wanting to exercise

Industry/Entity Type

Health And Wellness

Contact Information for Business Card

Megan Dorrit - Exercise Physiologist 0437 582 906
14 Larkspur Bend Rd
South Geelong
(Gate 2, Brannock Fitness)
vantorahealth@maildrop-example.com
socialpage-example.com/Vantora

Requirements
Must have
• I would like to include a section to add next appointment date and time space to the back of the card.
Nice to have
• Rounded corners and a black background on 1 or 2 sides.
Should not have
• Pictures of fit/toned bodies etc

```html
<!DOCTYPE html>
<html lang="en">
<head>
<meta charset="utf-8">
<title>Vantora Health &amp; Rehabilitation – Business Cards</title>
<link rel="stylesheet" href="https://fonts.googleapis.com/css2?family=Montserrat:wght@400;500&display=swap">
<style>
  :root {
    --page-bg: #eceeef;
    --card-bg: #ffffff;
    --brand-blue: #1a4fc0;
    --sky-blue: #5aa9dc;
    --deep-blue: #0b4fc4;
    --ink: #1d1d1f;
    --muted: #55585e;
    --card-shadow: 0 10px 30px rgba(0, 0, 0, 0.14);
  }
  * { box-sizing: border-box; margin: 0; padding: 0; }
  html, body {
    width: 1200px;
    height: 1200px;
    overflow: hidden;
    background: var(--page-bg);
    font-family: "Montserrat", Arial, sans-serif;
  }
  .sheet {
    width: 1200px;
    height: 1200px;
    display: flex;
    flex-direction: column;
    align-items: center;
    justify-content: center;
    gap: 60px;
  }
  .card {
    position: relative;
    width: 800px;
    height: 470px;
    background: var(--card-bg);
    box-shadow: var(--card-shadow);
    overflow: hidden;
  }
  .card-band {
    position: absolute;
    left: 0;
    right: 0;
    bottom: 0;
    height: 20px;
    display: flex;
  }
  .card-band .band-light { flex: 1; background: var(--sky-blue); }
  .card-band .band-gap { width: 6px; background: var(--card-bg); }
  .card-band .band-dark { width: 165px; background: var(--deep-blue); }

  .brand { display: flex; align-items: center; gap: 18px; }
  .brand-dot { border-radius: 50%; background: var(--sky-blue); flex: none; }
  .brand-text { display: flex; flex-direction: column; }
  .brand-name {
    color: var(--brand-blue);
    font-weight: 500;
    line-height: 1;
    letter-spacing: 0.5px;
  }
  .brand-tagline {
    color: var(--sky-blue);
    font-weight: 400;
    text-transform: uppercase;
    letter-spacing: 1.5px;
    margin-top: 8px;
  }

  /* Front */
  .card-front .brand {
    position: absolute;
    left: 50%;
    top: 46%;
    transform: translate(-50%, -50%);
  }
  .card-front .brand-dot { width: 92px; height: 92px; }
  .card-front .brand-name { font-size: 76px; }
  .card-front .brand-tagline { font-size: 15px; }

  /* Back */
  .card-back {
    display: flex;
    flex-direction: column;
    align-items: center;
    padding-top: 28px;
  }
  .card-back .brand-dot { width: 58px; height: 58px; }
  .card-back .brand-name { font-size: 44px; }
  .card-back .brand-tagline { font-size: 10px; margin-top: 6px; }
  .contact {
    margin-top: 16px;
    text-align: center;
    color: var(--ink);
    font-size: 17px;
    line-height: 1.3;
  }
  .contact-person { font-weight: 500; }
  .contact-icon {
    display: block;
    margin: 6px auto 4px;
    width: 15px;
    height: 15px;
  }
  .contact-online {
    margin-top: 10px;
    display: flex;
    justify-content: center;
    gap: 22px;
    font-size: 14px;
    color: var(--ink);
  }
  .contact-online span { display: inline-flex; align-items: center; gap: 6px; }
  .contact-online svg { width: 14px; height: 14px; flex: none; }

  .appointment {
    position: absolute;
    left: 60px;
    right: 60px;
    bottom: 44px;
    display: flex;
    align-items: flex-end;
    gap: 14px;
    font-size: 14px;
    color: var(--muted);
  }
  .appointment-title {
    font-weight: 500;
    color: var(--brand-blue);
    white-space: nowrap;
  }
  .appointment-field { display: flex; align-items: flex-end; gap: 8px; }
  .appointment-field.date { flex: 1.3; }
  .appointment-field.time { flex: 1; }
  .appointment-line {
    flex: 1;
    height: 1px;
    background: var(--sky-blue);
    margin-bottom: 4px;
  }
</style>
</head>
<body>
<main class="sheet">

  <section class="card card-front" aria-label="Card front">
    <div class="brand">
      <span class="brand-dot"></span>
      <div class="brand-text">
        <span class="brand-name">vantora</span>
        <span class="brand-tagline">Health &amp; Rehabilitation</span>
      </div>
    </div>
    <div class="card-band">
      <span class="band-light"></span>
      <span class="band-gap"></span>
      <span class="band-dark"></span>
    </div>
  </section>

  <section class="card card-back" aria-label="Card back">
    <div class="brand">
      <span class="brand-dot"></span>
      <div class="brand-text">
        <span class="brand-name">vantora</span>
        <span class="brand-tagline">Health &amp; Rehabilitation</span>
      </div>
    </div>
    <div class="contact">
      <p class="contact-person">Megan Dorrit -<br>Exercise Physiologist</p>
      <svg class="contact-icon" viewBox="0 0 16 16" aria-hidden="true">
        <circle cx="8" cy="8" r="8" fill="var(--deep-blue)"/>
        <path d="M5.2 4.2l1.4-.3.8 1.8-.9.7c.5 1.1 1.2 1.8 2.2 2.3l.7-.9 1.8.8-.3 1.4c-3.2.2-5.9-2.5-5.7-5.8z" fill="#fff"/>
      </svg>
      <p class="contact-phone">0437 582 906</p>
      <svg class="contact-icon" viewBox="0 0 16 16" aria-hidden="true">
        <circle cx="8" cy="8" r="8" fill="var(--deep-blue)"/>
        <path d="M8 3.5a3 3 0 0 1 3 3c0 2.2-3 5.8-3 5.8S5 8.7 5 6.5a3 3 0 0 1 3-3z" fill="#fff"/>
        <circle cx="8" cy="6.5" r="1.1" fill="var(--deep-blue)"/>
      </svg>
      <p class="contact-address">14 Larkspur Bend Rd, South Geelong<br>(Gate 2, Brannock Fitness)</p>
      <p class="contact-online">
        <span>
          <svg viewBox="0 0 16 16" aria-hidden="true">
            <circle cx="8" cy="8" r="8" fill="var(--deep-blue)"/>
            <rect x="4" y="5" width="8" height="6" rx="0.8" fill="#fff"/>
            <path d="M4.3 5.4L8 8.3l3.7-2.9" fill="none" stroke="var(--deep-blue)" stroke-width="0.9"/>
          </svg>
          vantorahealth@maildrop-example.com
        </span>
        <span>
          <svg viewBox="0 0 16 16" aria-hidden="true">
            <circle cx="8" cy="8" r="8" fill="var(--deep-blue)"/>
            <circle cx="8" cy="8" r="4" fill="none" stroke="#fff" stroke-width="1"/>
            <path d="M4 8h8M8 4c-1.6 2.4-1.6 5.6 0 8M8 4c1.6 2.4 1.6 5.6 0 8" fill="none" stroke="#fff" stroke-width="0.8"/>
          </svg>
          socialpage-example.com/Vantora
        </span>
      </p>
    </div>
    <div class="appointment">
      <span class="appointment-title">Next appointment</span>
      <span class="appointment-field date">Date <span class="appointment-line"></span></span>
      <span class="appointment-field time">Time <span class="appointment-line"></span></span>
    </div>
    <div class="card-band">
      <span class="band-light"></span>
      <span class="band-gap"></span>
      <span class="band-dark"></span>
    </div>
  </section>

</main>
</body>
</html>
```